Industrial Laundry News Paper Add

We need a color add for 1/4 page newspaper using blue and white. We are an industrial laundry providing linen washing for condo rental companies. We can provide linen rental and wash customer-owned goods

```html
<!DOCTYPE html>
<html lang="en">
<head>
<meta charset="utf-8">
<title>Summit Ridge Services – Industrial Laundry Ad</title>
<link rel="stylesheet" href="https://fonts.googleapis.com/css2?family=Open+Sans:wght@400;700;800&family=Antonio:wght@600&family=Jost:wght@300;500;600&display=swap">
<style>
  :root {
    --navy: #1f1a5e;
    --navy-band: #262f78;
    --blue: #27498f;
    --blue-soft: #5b79b0;
    --blue-light: #8fa6d8;
    --ink: #222;
    --white: #ffffff;
    --page: #e9ecf1;
  }
  * { margin: 0; padding: 0; box-sizing: border-box; }
  html, body { width: 872px; height: 1200px; overflow: hidden; background: var(--page); }
  .ad {
    position: absolute; left: 44px; top: 0;
    width: 784px; height: 1200px;
    background: var(--white); overflow: hidden;
  }
  .ad-artwork { position: absolute; inset: 0; width: 784px; height: 1200px; }

  .headline {
    position: absolute; left: 270px; top: 540px; width: 488px;
    font-family: "Open Sans", sans-serif; font-weight: 800;
    font-size: 43px; line-height: 51px; letter-spacing: -1.2px;
    color: var(--navy); text-align: center; text-transform: uppercase;
  }

  .services { position: absolute; left: 30px; top: 650px; list-style: none; }
  .service { display: flex; align-items: center; height: 67px; }
  .service-icon {
    width: 54px; height: 54px; border-radius: 50%;
    border: 1.5px solid var(--navy); margin-right: 14px;
    display: flex; align-items: center; justify-content: center;
  }
  .service-icon span {
    width: 36px; height: 36px; border-radius: 50%;
    background: radial-gradient(circle, #6f8fc4, #b9c8e2);
  }
  .service-name {
    font-family: "Antonio", sans-serif; font-weight: 600;
    font-size: 26px; line-height: 28px; color: var(--ink); text-transform: uppercase;
  }

  .about {
    position: absolute; left: 280px; top: 661px; width: 468px;
    font-family: "Open Sans", sans-serif; font-size: 17px; line-height: 25.3px;
    color: var(--ink); text-align: justify;
  }

  .offer {
    position: absolute; left: 41px; top: 880px; width: 420px;
    font-family: "Open Sans", sans-serif; font-weight: 700;
    font-size: 20.5px; line-height: 27.6px; color: var(--blue); text-transform: uppercase;
    letter-spacing: -0.2px;
  }

  .brand {
    position: absolute; left: 444px; top: 938px; width: 300px;
    font-family: "Open Sans", sans-serif; font-weight: 800;
    font-size: 32px; line-height: 38px; color: var(--navy); text-align: center;
    text-transform: uppercase;
  }

  .cta {
    position: absolute; left: 36px; top: 1018px; width: 314px; height: 37px;
    border-radius: 19px; background: var(--blue-soft); border: 2px solid var(--white);
    box-shadow: 0 5px 8px rgba(0,0,0,.35);
    font-family: "Jost", sans-serif; font-weight: 300; font-size: 22px; line-height: 33px;
    color: var(--white); text-align: center; text-transform: uppercase;
  }

  .contact { position: absolute; left: 29px; color: var(--white); font-family: "Jost", sans-serif; }
  .contact-phone { top: 1080px; font-weight: 600; font-size: 39px; line-height: 44px; }
  .contact-web { top: 1119px; font-weight: 600; font-size: 24.5px; line-height: 30px; color: var(--blue-light); }
  .contact-address { top: 1161px; font-weight: 500; font-size: 16.5px; line-height: 22px; }
  .contact-email { left: 498px; top: 1161px; font-weight: 500; font-size: 16.5px; line-height: 22px; }
</style>
</head>
<body>
<main class="ad">
  <svg class="ad-artwork" viewBox="0 0 784 1200" aria-hidden="false">
    <defs>
      <linearGradient id="washerTone" x1="0" y1="0" x2="1" y2="0.4">
        <stop offset="0" stop-color="#7d8388"/>
        <stop offset="0.35" stop-color="#b9bdc1"/>
        <stop offset="0.7" stop-color="#9ea3a8"/>
        <stop offset="1" stop-color="#d9dbde"/>
      </linearGradient>
      <linearGradient id="topWave" x1="0" y1="0" x2="1" y2="0">
        <stop offset="0" stop-color="#2a4ea0"/>
        <stop offset="1" stop-color="#7ba4cc"/>
      </linearGradient>
      <linearGradient id="lowerBand" x1="0" y1="0" x2="1" y2="0">
        <stop offset="0" stop-color="#2b4f9e"/>
        <stop offset="1" stop-color="#233f86"/>
      </linearGradient>
      <linearGradient id="linenTone" x1="0" y1="0" x2="1" y2="1">
        <stop offset="0" stop-color="#f6f7f9"/>
        <stop offset="1" stop-color="#d8dce4"/>
      </linearGradient>
      <linearGradient id="footerBand" x1="0" y1="0" x2="1" y2="0">
        <stop offset="0" stop-color="#252c78"/>
        <stop offset="1" stop-color="#2c4e9d"/>
      </linearGradient>
    </defs>

    <!-- top photo area -->
    <g role="img" aria-label="Photo of a row of stainless steel industrial washing machines">
      <path d="M0 0 H784 V400 C680 392 560 380 480 392 C340 440 170 488 0 505 Z" fill="url(#washerTone)"/>
    </g>
    <!-- top left light wave -->
    <path d="M0 0 H400 C330 20 250 95 150 97 C80 98 30 82 0 70 Z" fill="url(#topWave)"/>
    <!-- top right navy band -->
    <path d="M395 0 H784 V103 C700 45 560 10 420 12 C410 8 400 4 395 0 Z" fill="var(--navy-band)"/>

    <!-- lower navy band -->
    <path d="M0 520 C200 500 400 440 560 380 L784 380 V450 C600 470 430 540 260 570 C160 585 70 585 0 583 Z" fill="var(--navy-band)"/>
    <!-- lower blue band -->
    <path d="M0 499 C170 486 340 436 480 392 C600 378 700 388 784 398 V410 C680 410 560 420 471 440 C370 480 230 518 0 524 Z" fill="url(#lowerBand)"/>
    <!-- white swoosh -->
    <path d="M312 520 C380 492 430 465 480 440 C520 425 560 415 600 410 C550 425 470 460 312 520 Z" fill="var(--white)"/>

    <!-- circle photo -->
    <circle cx="603" cy="391" r="144" fill="var(--white)"/>
    <g role="img" aria-label="Photo of hands folding a stack of clean white linens">
      <circle cx="603" cy="391" r="129" fill="url(#linenTone)"/>
    </g>

    <!-- footer band -->
    <path d="M0 1048 C120 1020 250 1036 360 1058 C470 1082 560 1115 650 1118 C720 1120 760 1105 784 1090 V1200 H0 Z" fill="url(#footerBand)"/>
    <path d="M458 1080 C560 1112 680 1112 784 1062 V1076 C680 1128 560 1124 458 1080 Z" fill="var(--blue-soft)"/>
  </svg>

  <h1 class="headline">The first name in<br>industrial laundry</h1>

  <ul class="services">
    <li class="service">
      <div class="service-icon"><span role="img" aria-label="Carpet cleaning machine icon"></span></div>
      <p class="service-name">Carpet<br>cleaning</p>
    </li>
    <li class="service">
      <div class="service-icon"><span role="img" aria-label="Commercial laundry worker icon"></span></div>
      <p class="service-name">Commercial<br>laundry</p>
    </li>
    <li class="service">
      <div class="service-icon"><span role="img" aria-label="Housekeeping vacuuming icon"></span></div>
      <p class="service-name">Housekeeping in<br>Pine Hollow</p>
    </li>
  </ul>

  <p class="about">Summit Ridge Services is a family-owned and operated cleaning company. Our goal is to continued growth by offering customers a consistent, reliable total cleaning solution day in and day out. We always strive to combine industry experience with the latest cleaning technologies and environmentally friendly products — so you get the best possible results.</p>

  <p class="offer">Providing linen washing for<br>condo rental companies. We can<br>provide linen rental and wash<br>customer-owned goods</p>

  <p class="brand">Summit Ridge<br>Services</p>

  <p class="cta">Contact us today !</p>

  <p class="contact contact-phone">Call : 1 555-014-2870</p>
  <p class="contact contact-web">www.summitridgeservices.com</p>
  <p class="contact contact-address">48 Industry Way, Pine Hollow, CA 90000, USA</p>
  <p class="contact contact-email">info@summitridgeservices.com</p>
</main>
</body>
</html>
```